Velkano Holdings Ltd - An invesmtent & trading company needs a web design

We need a web design for our company based in Cyprus. The company was founded in 2009. We have continuously grown and now invest & trade all over the world.

Velkano Holdings ltd. specializes in the buying and selling of crude oil, precious metals and the investment in properties.

We know that trust is of the utmost importance when it comes to business and the design should communicate this to prospective business partners. Find attached the company logo. The colour scheme for the website should use similar colours and ideally incorporate the logo in some shape or form as well.

Target Market(s)

Oil Traders, Metall Traders, Property Investments

Industry/Entity Type

Trade

Coding

Coded - Design and coding required

Number of Pages Required

4 page

Font styles to use
Sans Serif

Requirements
Must have
• Mainpage,
• About Us
• Partners
• Legal Notice

```html
<!DOCTYPE html>
<html lang="en">
<head>
<meta charset="utf-8">
<title>Velkano Holdings Ltd</title>
<link href="https://fonts.googleapis.com/css2?family=Roboto:wght@300;400;500;700&display=swap" rel="stylesheet">
<style>
:root{
  --navy:#0b2a5c;
  --navy-dark:#071d43;
  --blue:#1c62b8;
  --blue-bright:#2a86d9;
  --sky:#4fa3e8;
  --ink:#2a2a2a;
  --muted:#666;
  --footer:#3a3b3d;
  --footer-dark:#2d2e30;
  --white:#fff;
}
*{box-sizing:border-box;margin:0;padding:0}
html,body{width:831px;height:1200px;overflow:hidden;background:#fff}
body{font-family:"Roboto",Arial,sans-serif;color:var(--ink);position:relative}

.site-header{height:110px;position:relative;background:#fff}
.brand{position:absolute;left:90px;top:22px;display:flex;align-items:center;gap:10px}
.brand-square{width:36px;height:36px;background:var(--navy)}
.brand-name{font-size:24px;font-weight:700;color:var(--navy);letter-spacing:1px;line-height:1}
.call{position:absolute;right:90px;top:22px;display:flex;align-items:center;gap:8px}
.call-text{font-size:10px;color:var(--blue)}
.call-text strong{display:block;font-size:16px;font-weight:500;color:var(--navy)}
.main-nav{position:absolute;right:0;top:66px;height:28px;width:430px;background:var(--navy);display:flex;padding-left:30px}
.main-nav a{font-size:11px;color:#fff;text-decoration:none;padding:0 16px;line-height:28px}
.main-nav a.active{background:var(--blue-bright)}

.hero{position:relative;height:290px;background:linear-gradient(180deg,#5f7a92 0%,#b98f62 45%,#e59a3c 62%,#3a3226 100%)}
.hero-arrow{position:absolute;top:130px;width:18px;height:22px;background:rgba(0,0,0,.55);color:#fff;font-size:12px;text-align:center;line-height:22px}
.hero-arrow.prev{left:0}.hero-arrow.next{right:0}
.hero-caption{position:absolute;left:90px;right:90px;bottom:0;background:rgba(28,98,184,.75);color:#fff;font-size:14px;font-weight:300;padding:8px 12px;line-height:1.35}

.about{text-align:center;padding:20px 90px 0;height:150px}
.about h2,.specialize h2{font-size:17px;font-weight:500;color:var(--navy);margin-bottom:10px}
.about h2 span{color:var(--blue-bright)}
.about p{font-size:8px;color:var(--muted);line-height:1.5}
.read-more{display:inline-block;font-size:8px;font-weight:700;color:var(--navy);margin-top:6px}

.specialize{height:300px;background:linear-gradient(180deg,var(--navy-dark) 0%,var(--blue) 60%,var(--sky) 100%);color:#fff;text-align:center;padding:18px 90px 0;position:relative}
.specialize h2{color:#fff}
.specialize p.lead{font-size:8px;line-height:1.5;opacity:.9}
.spec-name{position:absolute;left:50%;top:78px;transform:translateX(-50%);font-size:16px;font-weight:700;color:rgba(11,42,92,.55)}
.service{position:absolute;width:170px;text-align:center}
.service .icon{width:34px;height:34px;border-radius:50%;background:#fff;margin:0 auto 6px;display:flex;align-items:center;justify-content:center}
.service h3{font-size:10px;font-weight:500;margin-bottom:3px}
.service p{font-size:7.5px;line-height:1.4}
.service.oil{left:110px;top:110px}
.service.property{right:110px;top:110px}
.service.metals{left:330px;top:170px}
.btn-more{position:absolute;left:50%;bottom:12px;transform:translateX(-50%);background:#fff;color:var(--navy);font-size:8px;font-weight:700;padding:4px 10px;line-height:1.2}

.site-footer{height:350px;background:linear-gradient(180deg,var(--footer) 0%,var(--footer-dark) 100%);position:relative;color:#ddd}
.contact{position:absolute;left:90px;top:16px;width:220px}
.contact h4{font-size:11px;font-weight:500;color:#fff;border-bottom:1px solid #555;padding-bottom:6px;margin-bottom:10px}
.contact-row{display:flex;gap:8px;margin-bottom:12px;font-size:8px;line-height:1.45}
.contact-row .dot{width:12px;height:12px;flex:none}
.contact-row b{color:#fff;font-weight:500;display:block}
.footer-name{position:absolute;left:300px;top:150px;font-size:28px;font-weight:700;color:rgba(255,255,255,.12)}
.inquiry{position:absolute;right:90px;top:16px;width:220px;background:#55575a;padding:0 0 12px}
.inquiry h4{background:#4a4c4f;font-size:11px;font-weight:500;color:#fff;padding:7px 10px;display:flex;align-items:center;gap:8px}
.inquiry h4 i{width:14px;height:14px;border-radius:50%;border:2px solid #fff;display:inline-block}
.inquiry p{font-size:7px;padding:6px 10px;color:#ddd}
.field{display:flex;align-items:center;margin:0 10px 6px;font-size:7px}
.field label{width:45px}
.field span{flex:1;height:14px;background:#eee}
.field.msg span{height:40px}
.submit{margin:6px 0 0 55px;display:inline-block;background:var(--navy);color:#fff;font-size:8px;font-weight:700;padding:4px 12px}

.copyright{position:absolute;left:0;right:0;bottom:0;height:30px;background:var(--navy-dark);color:#aab;font-size:7.5px;text-align:center;line-height:30px}
</style>
</head>
<body>
<header class="site-header">
  <div class="brand"><div class="brand-square"></div><div class="brand-name">VELKANO HOLDINGS LTD</div></div>
  <div class="call">
    <svg width="20" height="20" viewBox="0 0 24 24"><circle cx="12" cy="12" r="12" fill="#1c62b8"/><path d="M8 6l2 0 1 3-1.5 1a7 7 0 0 0 4 4l1-1.5 3 1v2a2 2 0 0 1-2 2A10 10 0 0 1 6 8a2 2 0 0 1 2-2z" fill="#fff"/></svg>
    <div class="call-text">Call Us Today<strong>123-456-7890</strong></div>
  </div>
  <nav class="main-nav"><a class="active">Home</a><a>About</a><a>Partners</a><a>Legal Notice</a><a>Contact</a></nav>
</header>

<section class="hero" role="img" aria-label="Oil pump jacks silhouetted against a sunset sky">
  <span class="hero-arrow prev">&#8249;</span><span class="hero-arrow next">&#8250;</span>
  <div class="hero-caption">We Specialize in the buying and selling of crude oil, precious metals and the investment in properties.</div>
</section>

<section class="about">
  <h2>About <span>Velkano Holdings Ltd.</span></h2>
  <p>Lorem ipsum dolor sit amet, consectetuer adipiscing elit, sed diam nonummy nibh euismod tincidunt ut laoreet dolore magna aliquam erat volutpat. Ut wisi enim ad minim veniam, quis nostrud exerci tation ullamcorper suscipit lobortis nisl ut aliquip ex ea commodo consequat. Duis autem vel eum iriure dolor in hendrerit in vulputate velit esse molestie consequat, vel illum dolore eu feugiat nulla facilisis at vero eros et accumsan et iusto odio dignissim qui blandit praesent luptatum zzril delenit augue duis dolore te feugait nulla facilisi.</p>
  <span class="read-more">Read More</span>
</section>

<section class="specialize">
  <h2>We Specialize In The Buying And Selling Of</h2>
  <p class="lead">Lorem ipsum dolor sit amet, consectetuer adipiscing elit, sed diam nonummy nibh euismod tincidunt ut laoreet dolore magna aliquam erat volutpat. Ut wisi enim ad minim veniam, quis nostrud exerci tation ullamcorper suscipit.</p>
  <div class="spec-name">VELKANO</div>
  <div class="service oil">
    <div class="icon"><svg width="16" height="18" viewBox="0 0 16 20"><path d="M8 1C8 1 2 9 2 13a6 6 0 0 0 12 0C14 9 8 1 8 1z" fill="#1c62b8"/></svg></div>
    <h3>Crude Oil</h3><p>Lorem ipsum dolor sit amet, consectetuer adipiscing elit, sed diam nonummy nibh euismod</p>
  </div>
  <div class="service property">
    <div class="icon"><svg width="18" height="16" viewBox="0 0 20 18"><path d="M10 1L1 9h3v8h4v-5h4v5h4V9h3z" fill="#1c62b8"/></svg></div>
    <h3>Investments In Properties</h3><p>Lorem ipsum dolor sit amet, consectetuer adipiscing elit, sed diam nonummy nibh euismod</p>
  </div>
  <div class="service metals">
    <div class="icon"><svg width="18" height="14" viewBox="0 0 20 14"><path d="M4 2h12l3 10H1z" fill="#1c62b8"/></svg></div>
    <h3>Precious Metals</h3><p>Lorem ipsum dolor sit amet, consectetuer adipiscing elit, sed diam nonummy nibh euismod</p>
  </div>
  <span class="btn-more">Read More</span>
</section>

<footer class="site-footer">
  <div class="contact">
    <h4>Contact Information</h4>
    <div class="contact-row"><svg class="dot" viewBox="0 0 12 12"><path d="M6 0a4 4 0 0 0-4 4c0 3 4 8 4 8s4-5 4-8a4 4 0 0 0-4-4z" fill="#fff"/></svg><div><b>Main Office</b>Street Name, City Name<br>State Zip code</div></div>
    <div class="contact-row"><svg class="dot" viewBox="0 0 12 12"><path d="M3 1h2l1 3-1 1a5 5 0 0 0 2 2l1-1 3 1v2a1 1 0 0 1-1 1A9 9 0 0 1 2 2a1 1 0 0 1 1-1z" fill="#fff"/></svg><div><b>Telephone</b>123-456-7890</div></div>
    <div class="contact-row"><svg class="dot" viewBox="0 0 12 12"><rect x="1" y="3" width="10" height="7" fill="#fff"/><path d="M1 3l5 4 5-4" stroke="#3a3b3d" fill="none"/></svg><div><b>Email</b>info@velkanoholdings.com</div></div>
    <div class="contact-row"><svg class="dot" viewBox="0 0 12 12"><circle cx="6" cy="6" r="6" fill="#fff"/></svg><div><b>Facebook</b>facebook.com/velkanoholdings</div></div>
  </div>
  <div class="footer-name">VELKANO</div>
  <div class="inquiry">
    <h4><i></i>QUICK INQUIRY</h4>
    <p>We will endeavor to answer your inquiry within 24 hours.</p>
    <div class="field"><label>Name</label><span></span></div>
    <div class="field"><label>Email</label><span></span></div>
    <div class="field"><label>Phone</label><span></span></div>
    <div class="field msg"><label>Message</label><span></span></div>
    <span class="submit">SUBMIT</span>
  </div>
  <div class="copyright">© 2014 Velkano Holdings Ltd. - All Rights Reserved</div>
</footer>
</body>
</html>
```